Web Design Project

8 page static website.
About us/What we stand for:
Forno Lucente CBD plans to make a huge splash in Sydney by being the first Italian pizza and pasta retail food outlet offering truly fresh, nutritious ingredients – herbs and vegetables are picked directly from the garden, pizzas are made with love in a fun filled atmosphere and a cutting edge brand strategy that promotes a happy lifestyle and reminds people that happiness and togetherness comes from sharing amazing food.
The best thing about Forno Lucente is that it offers consumers a choice to either choose from the enticing gluten free and vegetarian menu range to the more traditional pizza and pasta, we cater for their own tastes, this provides a distinct point of difference in the retail food market, as well as allowing consumers to have an endless range of choices without having to worry about the nutritional value.
Consumers have now become accustomed to a consistent brand experience which is setting increasingly high standards when it comes to food quality, taste and service.
We want to capitalise on the opportunity to create a strong, modern brand that promotes healthy lifestyle habits, sells fresh, wholesome ingredients, delivers
exceptional service in a fun filled atmosphere and appeals to a broad market.
Our business model is specifically pickup and delivery with a few seats and crates for eating in. It is for the time poor that still want to have a great tasting Italian experience with pizza and pasta within the quick service restaurant space. Takeaway, office catering and delivery will be a large percentage of our business.
Our philosophy at Forno Lucente is simple:
“Success is not a formula, it’s a recipe”.
Brand personality:
We are located in a laneway and basically the shop is a hole in the one. It looks like a restaurant you would see in Italy.
Modern Italian, contemporary, fun, rustic (Tico Taco, Brasa’d)
1 Aims of this website
• Emotionally connect with the target audience to reflect (“happiness and togetherness comes from sharing amazing food”)
• To entice people to order pizza
• To capture a mailing list
• To differentiate us from the low cost, low quality pizza
• To create a connection with the target audience, and promote word of mouth
2 Target audience(s)
• Male/Female
• 18-49
• Sydney CBD and Woolloomooloo
• Internet Savvy.
3. Contents/Functionality
www.crustwander.com.au – like the rustic brown in the website and the old washed out white colour through the font.
Target Market(s)
18-49 years old
City worker and resident
people that enjoy good food
Industry/Entity Type
Restaurant
Requirements
Must have
- Some splash of red and green to represent the italian theme.
Nice to have
- Please see http://www.brasad-example.com.au/Pages/locationmenu.aspx
This is how our takeaway menu looks like.

```html
<!DOCTYPE html>
<html lang="en">
<head>
<meta charset="utf-8">
<title>Forno Lucente – Caffè Pizzeria</title>
<link href="https://fonts.googleapis.com/css2?family=Marcellus+SC&family=Arimo:wght@400&display=swap" rel="stylesheet">
<style>
  :root {
    --bg-dark: #1f1510;
    --bg-mid: #33241c;
    --bar-top: #6a4d40;
    --bar-bottom: #3b2a22;
    --tab: #6e5446;
    --tab-dark: #56402f;
    --cream: #f1e7da;
    --muted: #d9cbbb;
    --red: #c0321f;
    --green: #5aa83a;
    --orange: #f08a1c;
    --frame: #8a6a4e;
    --card: #2b201a;
    --card-border: #5a4638;
    --panel: #271d18;
    --rule: #4a3a2e;
  }
  * { box-sizing: border-box; margin: 0; padding: 0; }
  html, body { width: 1094px; height: 1200px; overflow: hidden; }
  body {
    position: relative;
    font-family: "Arimo", Arial, sans-serif;
    color: var(--cream);
    background:
      radial-gradient(ellipse at 50% 30%, var(--bg-mid) 0%, var(--bg-dark) 75%);
  }
  .top-bar {
    position: absolute; left: 0; top: 0; width: 1094px; height: 40px;
    background: linear-gradient(var(--bar-top), var(--bar-bottom));
    box-shadow: 0 2px 6px rgba(0,0,0,.6);
  }
  .follow {
    position: absolute; left: 718px; top: 11px;
    font-family: "Marcellus SC", serif; font-size: 16px; letter-spacing: 1px; color: var(--cream);
  }
  .social { position: absolute; top: 5px; width: 30px; height: 30px; border-radius: 50%; background: #1e1612; border: 2px solid #4f3a2e; }
  .order-now {
    position: absolute; right: 135px; top: 56px;
    font-family: "Marcellus SC", serif; font-size: 16px; letter-spacing: 1px; color: var(--cream);
  }
  .brand {
    position: absolute; left: 140px; top: 78px; display: flex; align-items: center; gap: 10px;
  }
  .brand-mark { width: 36px; height: 36px; border-radius: 50%; background: var(--cream); }
  .brand-name { font-family: "Marcellus SC", serif; font-size: 24px; color: var(--cream); line-height: 1.1; }
  .nav { position: absolute; left: 372px; top: 108px; display: flex; gap: 4px; }
  .nav a {
    display: block; width: 144px; height: 39px; text-decoration: none;
    font-family: "Marcellus SC", serif; font-size: 17px; letter-spacing: 1px; color: var(--cream);
    text-align: center; line-height: 39px;
    background: linear-gradient(var(--tab), var(--tab-dark));
    clip-path: polygon(0 0, 94% 0, 100% 100%, 4% 100%);
  }
  .nav a.active { box-shadow: inset 0 -3px 0 var(--red); }
  .hero-frame {
    position: absolute; left: 129px; top: 185px; width: 501px; height: 332px;
    background: var(--frame); box-shadow: 0 3px 8px rgba(0,0,0,.6);
  }
  .hero-photo {
    position: absolute; left: 10px; top: 9px; width: 483px; height: 315px;
    background: linear-gradient(135deg, #e8d2a6 0%, #d9b672 45%, #b5652e 80%, #7d4a2a 100%);
  }
  .slider-dots { position: absolute; right: 16px; bottom: 8px; display: flex; gap: 3px; }
  .slider-dots span { width: 13px; height: 13px; border-radius: 50%; background: var(--green); }
  .slider-dots span.current { background: var(--orange); }
  .intro {
    position: absolute; left: 650px; top: 184px; width: 305px;
    font-size: 15px; line-height: 18.5px; text-align: justify; color: var(--cream);
  }
  .rule { position: absolute; left: 188px; width: 735px; height: 1px; background: var(--rule); }
  .feature {
    position: absolute; top: 604px; width: 170px; height: 101px;
    background: var(--card); border: 3px solid var(--card-border); border-radius: 6px;
    text-align: center; font-family: "Marcellus SC", serif; font-size: 16px; letter-spacing: 1px; line-height: 18px;
    color: var(--cream);
  }
  .feature-art { width: 60px; height: 52px; margin: 6px auto 2px; border-radius: 6px; }
  .feature-label { position: absolute; left: 0; right: 0; bottom: 8px; }
  .club-title { margin-top: 8px; }
  .club-form { margin-top: 6px; text-align: left; padding-left: 3px; font-size: 12px; }
  .club-form label { display: flex; align-items: center; gap: 4px; height: 19px; }
  .club-form span { display: inline-block; width: 112px; height: 13px; border: 1px solid #5b4637; background: #221812; margin-left: auto; margin-right: 6px; }
  .section-title {
    position: absolute; left: 130px; top: 763px;
    font-family: "Marcellus SC", serif; font-size: 16px; letter-spacing: 1px; color: var(--red);
  }
  .testimonial {
    position: absolute; left: 129px; width: 834px; height: 144px;
    background: var(--panel); border-radius: 8px;
  }
  .quote-icon { position: absolute; left: 11px; top: 20px; }
  .testimonial p {
    position: absolute; left: 48px; top: 18px; width: 770px;
    font-size: 15px; line-height: 18.5px; text-align: justify;
  }
  .testimonial cite {
    position: absolute; right: 18px; top: 98px; font-style: normal;
    font-size: 15px; line-height: 18.5px; text-align: right;
  }
</style>
</head>
<body>
  <header class="top-bar">
    <span class="follow">Fallow us on:</span>
    <span class="social" style="left:849px" role="img" aria-label="Social profile link"></span>
    <span class="social" style="left:891px" role="img" aria-label="Social profile link"></span>
    <span class="social" style="left:934px" role="img" aria-label="Social profile link"></span>
  </header>

  <div class="order-now">Order now - 98XXXXXXXXX</div>

  <div class="brand">
    <span class="brand-mark"></span>
    <span class="brand-name">Forno Lucente</span>
  </div>

  <nav class="nav">
    <a class="active" href="#">Home</a>
    <a href="#">Anout us</a>
    <a href="#">Menu</a>
    <a href="#">Contact us</a>
  </nav>

  <section class="hero-frame">
    <div class="hero-photo" role="img" aria-label="Close-up of a pizza slice with stretched melted cheese, olives and mushrooms">
      <div class="slider-dots"><span></span><span></span><span></span><span class="current"></span></div>
    </div>
  </section>

  <p class="intro">It is a long established fact that a reader will be distracted by the readable content of a page when looking at its layout. The point of using Lorem Ipsum is that it has a more-or-less normal distribution of letters, as opposed to using 'Content here, content here', making it look like readable English. Many desktop publishing packages and web page editors now use Lorem Ipsum as their default model text, and a search for 'lorem ipsum' will un-cover many web sites still in their infancy. Various versions have evolved over the years, sometimes by accident, sometimes on purpose (injected humour and the like).</p>

  <div class="rule" style="top:565px"></div>

  <a class="feature" style="left:129px">
    <div class="feature-art" style="background:#4a3a30" role="img" aria-label="Online ordering badge illustration"></div>
    <div class="feature-label">Click here<br>to order online</div>
  </a>
  <div class="feature" style="left:351px">
    <div class="club-title">Join our<br>email club</div>
    <div class="club-form">
      <label>Name:<span></span></label>
      <label>Email:<span></span></label>
    </div>
  </div>
  <a class="feature" style="left:572px">
    <div class="feature-art" style="background:#1c1512" role="img" aria-label="Chef hat with fork and spoon illustration"></div>
    <div class="feature-label">Office Catering</div>
  </a>
  <a class="feature" style="left:794px">
    <div class="feature-art" style="background:linear-gradient(135deg,#c9a98a,#8a5a40)" role="img" aria-label="Delivery area map illustration"></div>
    <div class="feature-label">Delivery Area</div>
  </a>

  <div class="rule" style="top:747px"></div>

  <h2 class="section-title">Testimonial</h2>

  <article class="testimonial" style="top:802px">
    <svg class="quote-icon" width="20" height="17" viewBox="0 0 20 17" aria-hidden="true"><path d="M2 1h16v11H9l-4 4v-4H2z" fill="none" stroke="#8a7868" stroke-width="1.5"/></svg>
    <p>It is a long established fact that a reader will be distracted by the readable content of a page when looking at its layout. The point of using Lorem Ipsum is that it has a more-or-less normal distribution of letters, as opposed to using 'Content here, content here', making it look like readable English. Many desktop publishing packages and web page editors now use Lorem Ipsum as their default .</p>
    <cite>- Lorem Ipsum<br>Lorem Ipsum</cite>
  </article>

  <article class="testimonial" style="top:962px">
    <svg class="quote-icon" width="20" height="17" viewBox="0 0 20 17" aria-hidden="true"><path d="M2 1h16v11H9l-4 4v-4H2z" fill="none" stroke="#8a7868" stroke-width="1.5"/></svg>
    <p>It is a long established fact that a reader will be distracted by the readable content of a page when looking at its layout. The point of using Lorem Ipsum is that it has a more-or-less normal distribution of letters, as opposed to using 'Content here, content here', making it look like readable English. Many desktop publishing packages and web page editors now use Lorem Ipsum as their default .</p>
    <cite>- Lorem Ipsum<br>Lorem Ipsum</cite>
  </article>
</body>
</html>
```